Lumen Cove Skincare - Package Design

New Beauty label needing product packaging design. Looking for elegant and stylish design to represent our premium brand.

This project is for 1 label and 1 box design. The winning designer will be assigned another project for the next product in the range. (to be paid as a new project)

This product is for "Dead Sea Mud Mask". Please see the label format and jar attached. Please note there are 2 different jars we are considering (will have a mud inside). Please feel free to choose whichever one suits your design best.

The labels and boxes are to retain the product information, such as size, ingredients etc, but is to be updated to our brand. You can move or display the other information as you wish.

the size of the dead sea mud mask color box is 72*72*85mm (length*width*height)
the size of dead sea mud mask label is 218*58mm (width*height)

Target Market(s)

Women 15 to 65

Requirements
Must have
• Must be elegant and represent our brand which is a premium beauty product.
Should not have
• Dark blue. Dark purple etc. Colours should compliment the logo

```html
<!DOCTYPE html>
<html lang="en">
<head>
<meta charset="UTF-8">
<title>Lumen Cove Skincare – Dead Sea Mud Mask Label</title>
<link href="https://fonts.googleapis.com/css2?family=Source+Sans+3:wght@400;600;700&display=swap" rel="stylesheet">
<style>
  :root {
    --backdrop: #c4c7c6;
    --gold-deep: #a97a45;
    --gold-mid: #c89a5f;
    --gold-light: #f0c88e;
    --panel: #ffffff;
    --ink: #1a1a1d;
    --brand-gold: #b8893f;
  }
  html, body {
    margin: 0;
    padding: 0;
    width: 1200px;
    height: 924px;
    overflow: hidden;
    background: var(--backdrop);
    font-family: "Source Sans 3", sans-serif;
  }
  .canvas {
    position: relative;
    width: 1200px;
    height: 924px;
  }
  .label-band {
    position: absolute;
    left: 0;
    top: 298px;
    width: 1200px;
    height: 328px;
    background: linear-gradient(90deg,
      var(--gold-deep) 0%,
      var(--gold-mid) 18%,
      var(--gold-deep) 32%,
      var(--gold-mid) 48%,
      var(--gold-light) 62%,
      var(--gold-mid) 80%,
      var(--gold-deep) 100%);
  }
  .label-panel {
    position: absolute;
    left: 461px;
    top: 34px;
    width: 282px;
    height: 268px;
    background: var(--panel);
    box-shadow: 4px 4px 10px rgba(0,0,0,0.18);
  }
  .label-frame {
    position: absolute;
    inset: 9px;
    border: 2.5px solid var(--ink);
  }
  .brand-name {
    position: absolute;
    left: 0;
    right: 0;
    top: 48px;
    text-align: center;
    font-weight: 600;
    font-size: 15px;
    letter-spacing: 0.5px;
    color: var(--brand-gold);
  }
  .product-title {
    position: absolute;
    left: 0;
    right: 0;
    top: 114px;
    text-align: center;
    font-weight: 700;
    font-size: 23px;
    letter-spacing: -0.3px;
    color: var(--ink);
    margin: 0;
  }
  .title-rule {
    position: absolute;
    left: 91px;
    top: 157px;
    width: 99px;
    height: 2px;
    background: var(--ink);
  }
  .benefits {
    position: absolute;
    left: 0;
    right: 0;
    top: 170px;
    margin: 0;
    padding: 0;
    list-style: none;
    text-align: center;
    font-size: 13.5px;
    line-height: 20px;
    color: var(--ink);
  }
</style>
</head>
<body>
  <div class="canvas">
    <div class="label-band" role="img" aria-label="Metallic gold label background with fine geometric line pattern">
      <div class="label-panel">
        <div class="label-frame"></div>
        <div class="brand-name">Lumen Cove Skincare</div>
        <h1 class="product-title">DEAD SEA MUD MASK</h1>
        <div class="title-rule"></div>
        <ul class="benefits">
          <li>Anti Acne</li>
          <li>Deep Skin Cleanser</li>
          <li>Pore Reducer</li>
        </ul>
      </div>
    </div>
  </div>
</body>
</html>
```